Business Cards for a Junk Removal Company

Hello,
We are looking to have business cards designed that are simple, bold, easy to read, and right to the point. Please see the attachments for our logo files. We want the card to be yellow on both sides ( Color code Yellow: #FFE01B). The logo text font is (Rockstar Extra Bold) and this is also in the files attached. Please make the text black for the logo. On the back side of the card, you can use white and black for text. Thank you in advance for your hard work!

Front of card-
Harbor Haul Away (logo)
Back of card-
Harbor Haul Away
Donate - Recycle - Dispose
555-271-8093
www.harborhaulaway.example
info@harborhaulaway.example

Industry/Entity Type

Junk removal

Contact Information for Business Card

FRONT OF CARD- Harbor Haul Away (logo) BACK OF CARD- Harbor Haul Away Donate - Recycle - Dispose 555-271-8093 www.harborhaulaway.example info@harborhaulaway.example

Font styles to use
Other font styles liked:
• Rockstar Extra Bold

Colors
FFF300
FFF600
FEFA6F
FFFEC7
FFFEE8

Requirements
Must have
• Must have color code Yellow: #FFE01B for the background of front and back of the card

```html
<!DOCTYPE html>
<html lang="en">
<head>
<meta charset="utf-8">
<title>Harbor Haul Away — Business Cards</title>
<link rel="stylesheet" href="https://fonts.googleapis.com/css2?family=Anton&family=Roboto:wght@500&display=swap">
<style>
  :root {
    --yellow: #FFE01B;
    --black: #000000;
    --white: #ffffff;
    --stage: #4a2f22;
  }
  * { margin: 0; padding: 0; box-sizing: border-box; }
  html, body {
    width: 1200px;
    height: 1200px;
    overflow: hidden;
    background: var(--stage);
  }
  .card {
    position: absolute;
    left: 250px;
    width: 700px;
    height: 400px;
    background: var(--yellow);
    overflow: hidden;
  }
  .card--back { top: 170px; }
  .card--front { top: 631px; }

  .contact-panel {
    position: absolute;
    left: 0; top: 0;
    width: 345px;
    height: 400px;
    background: var(--black);
    padding-left: 41px;
  }
  .contact-panel .person-name {
    position: absolute;
    left: 41px; top: 97px;
    font-family: "Anton", sans-serif;
    font-size: 38px;
    line-height: 1;
    color: var(--yellow);
    letter-spacing: 0.5px;
  }
  .contact-panel .person-title {
    position: absolute;
    left: 41px; top: 140px;
    font-family: "Roboto", sans-serif;
    font-weight: 500;
    font-size: 19px;
    color: var(--white);
  }
  .contact-panel .contact-line {
    position: absolute;
    left: 41px;
    font-family: "Roboto", sans-serif;
    font-weight: 500;
    color: var(--white);
    letter-spacing: 0.3px;
    white-space: nowrap;
  }
  .contact-line--phone { top: 181px; font-size: 19px; }
  .contact-line--email { top: 209px; font-size: 16.5px; }
  .contact-line--web { top: 234px; font-size: 16.5px; }

  .tagline {
    position: absolute;
    left: 41px; top: 279px;
    display: flex;
    align-items: center;
    gap: 8px;
    font-family: "Anton", sans-serif;
    font-size: 18px;
    letter-spacing: 0.6px;
    color: var(--yellow);
  }
  .tagline .divider {
    width: 6px; height: 6px;
    background: var(--yellow);
  }

  .brand-name {
    position: absolute;
    font-family: "Anton", sans-serif;
    color: var(--black);
    white-space: nowrap;
    text-align: center;
    line-height: 1;
    transform: translate(-50%, -50%);
  }
  .card--back .brand-name {
    left: 522px; top: 200px;
    font-size: 34px;
    letter-spacing: 0.5px;
  }
  .card--front .brand-name {
    left: 350px; top: 200px;
    font-size: 72px;
    letter-spacing: 1px;
  }
</style>
</head>
<body>
  <section class="card card--back" aria-label="Business card, contact side">
    <div class="contact-panel">
      <p class="person-name">DANA REYES</p>
      <p class="person-title">CEO&amp;Founder</p>
      <p class="contact-line contact-line--phone">Ph. 555-271-8093</p>
      <p class="contact-line contact-line--email">info@harborhaulaway.example</p>
      <p class="contact-line contact-line--web">www.harborhaulaway.example</p>
      <p class="tagline">
        <span>DONATE</span><span class="divider"></span>
        <span>RECYCLE</span><span class="divider"></span>
        <span>DISPOSE</span>
      </p>
    </div>
    <p class="brand-name">HARBOR HAUL AWAY</p>
  </section>

  <section class="card card--front" aria-label="Business card, brand side">
    <p class="brand-name">HARBOR HAUL AWAY</p>
  </section>
</body>
</html>
```